Harbor's Hymn Single Cover for TuneVault etc

I am releasing a single out and I would like a simple cover design. This single cover will only be used online I.e. TuneVault Streamora . I am going for a simple hipster rustic look. I have attached my photo that should be included in the design. If possible I would rather the photo just edited and words added . Thank you

Target Market(s)

Teens to 40s contempary Christians

Industry/Entity Type

Music Download

Requirements
Must have
• -The picture below
• -Marisol Penrose
• -Harbor's hymn

```html
<!DOCTYPE html>
<html lang="en">
<head>
<meta charset="utf-8">
<title>Harbor’s Hymn — Marisol Penrose</title>
<link rel="stylesheet" href="https://fonts.googleapis.com/css2?family=Montserrat:wght@900&display=swap">
<style>
  :root {
    --band-coral: #f2737b;
    --band-plum: #8b5387;
    --photo-light: #e6e2d8;
    --photo-mid: #6a6e5a;
    --photo-green: #3f4a36;
    --photo-dark: #231e1d;
  }
  html, body {
    margin: 0;
    padding: 0;
    width: 1200px;
    height: 1200px;
    overflow: hidden;
    background: var(--band-coral);
  }
  .cover {
    display: block;
    width: 1200px;
    height: 1200px;
  }
  .band-title { fill: var(--band-coral); }
  .band-artist { fill: var(--band-plum); }
  .cover-word {
    font-family: "Montserrat", "Arial Black", sans-serif;
    font-weight: 900;
    fill: url(#photo-tones);
  }
</style>
</head>
<body>
<svg class="cover" viewBox="0 0 1200 1200" xmlns="http://www.w3.org/2000/svg">
  <defs>
    <linearGradient id="photo-tones" gradientUnits="userSpaceOnUse" x1="0" y1="0" x2="1200" y2="1200">
      <stop offset="0" stop-color="var(--photo-light)"/>
      <stop offset="0.35" stop-color="var(--photo-mid)"/>
      <stop offset="0.6" stop-color="var(--photo-green)"/>
      <stop offset="1" stop-color="var(--photo-dark)"/>
    </linearGradient>
  </defs>

  <rect class="band-title" x="0" y="0" width="1200" height="612"/>
  <rect class="band-artist" x="0" y="612" width="1200" height="588"/>

  <g role="img" aria-label="Portrait photo of the smiling singer outdoors, trees and road behind her, seen through the lettering">
    <text class="cover-word title-line-one" x="18" y="234" font-size="300" textLength="1164" lengthAdjust="spacingAndGlyphs">HARBOR’S</text>
    <text class="cover-word title-line-two" x="18" y="594" font-size="480" textLength="1164" lengthAdjust="spacingAndGlyphs">HYMN</text>
    <text class="cover-word artist-first" x="18" y="876" font-size="351" textLength="1164" lengthAdjust="spacingAndGlyphs">MARISOL</text>
    <text class="cover-word artist-last" x="18" y="1182" font-size="403" textLength="1164" lengthAdjust="spacingAndGlyphs">PENROSE</text>
  </g>
</svg>
</body>
</html>
```